Power point Presentation Template 2

I am looking a professionally designed Powerpoint Presentation template for my company. We are Information Technology Company. I have attached the Logo. The Logo will also give an indication of which colours to be used in the design.

Information and Communication Technology

• All ideas welcomed
• Professional Look and Feel

```html
<!DOCTYPE html>
<html lang="en">
<head>
<meta charset="utf-8">
<title>Nexora Technologies – Presentation Template</title>
<link rel="stylesheet" href="https://fonts.googleapis.com/css2?family=Open+Sans:wght@400;600;700;800&display=swap">
<style>
:root{
  --orange:#f7941d;
  --orange-deep:#e8810c;
  --ink:#222222;
  --dark:#2b2b2b;
  --darker:#1d1d1d;
  --grey:#777777;
  --light:#f3f3f3;
  --white:#ffffff;
}
*{box-sizing:border-box;margin:0;padding:0}
html,body{width:1200px;height:2287px;overflow:hidden;background:#d9d9d9}
body{font-family:"Open Sans",Arial,sans-serif;color:var(--ink)}
.sheet{width:1200px;height:2287px;display:grid;grid-template-columns:repeat(3,1fr);grid-template-rows:repeat(10,1fr);gap:2px}
.slide{position:relative;overflow:hidden;background:var(--white)}
.title{position:absolute;left:20px;top:10px;font-weight:700;font-size:14px;color:var(--ink)}
.title::after{content:"";display:block;width:24px;height:2px;background:var(--orange);margin-top:3px}
.foot{position:absolute;left:0;right:0;bottom:0;height:11px;background:var(--dark);display:flex;align-items:center;justify-content:space-between;padding:0 12px;font-size:4.5px;color:#bbb}
.foot .mark{color:var(--orange);font-weight:700;font-size:5px;letter-spacing:.5px}
.tx{font-size:5px;line-height:1.5;color:var(--grey)}
.tx.light{color:#ddd}
.ph{position:absolute}
.ph-blue{background:linear-gradient(135deg,#0b2440,#2c6a98 60%,#7fb2d6)}
.ph-dark{background:linear-gradient(135deg,#1f1f1f,#4d4d4d)}
.ph-city{background:linear-gradient(180deg,#c7d2dc,#8596a6)}
.ph-warm{background:linear-gradient(135deg,#3a3a3a,#8a7a66 70%,#d8a460)}
.ph-hand{background:linear-gradient(135deg,#0f2136,#3d6584 60%,#a9c4d8)}
.brand{font-weight:800;color:var(--orange);letter-spacing:1px;display:flex;align-items:center;gap:4px}
.brand .dot{width:9px;height:9px;border-radius:50%;background:var(--orange)}
.brand.white{color:var(--white)}
.brand.white .dot{background:var(--white)}
.bul{list-style:none}
.bul li{position:relative;padding-left:7px;margin-bottom:5px}
.bul li::before{content:"";position:absolute;left:0;top:2px;width:3px;height:3px;background:var(--orange)}
.h-sm{font-size:6px;font-weight:700;color:var(--ink)}
.h-sm.white{color:var(--white)}
.icon{display:inline-block;width:10px;height:10px;border-radius:50%;background:var(--orange)}

/* cover */
.cover .brand{position:absolute;left:88px;top:78px;font-size:34px;flex-direction:row;line-height:1}
.cover .brand .dot{width:26px;height:26px}
.cover .brand small{display:block;font-size:11px;letter-spacing:6px;margin-top:4px}
.dark-bg{background:linear-gradient(135deg,#1b1b1b,#3a3a3a)}
.hero-title{position:absolute;left:18px;top:110px;color:var(--white);font-size:22px;font-weight:700}
.hero-sub{position:absolute;left:18px;top:138px;color:var(--orange);font-size:7px}
.hero-url{position:absolute;left:18px;bottom:18px;color:#aaa;font-size:5px}
.slide .brand.top{position:absolute;left:18px;top:58px;font-size:14px}

/* agenda */
.agenda{position:absolute;left:50px;top:42px;right:20px;display:grid;grid-template-columns:1fr 1fr;gap:10px 30px}
.agenda .item{display:flex;gap:8px}
.agenda .sq{width:10px;height:10px;background:var(--dark);flex:none;margin-top:2px}
.agenda .item:nth-child(3) .sq,.agenda .item:nth-child(4) .sq{background:var(--orange)}
.agenda b{display:block;font-size:7px;font-weight:600}
.agenda b.o{color:var(--orange)}

/* chart slide columns */
.two{position:absolute;left:20px;right:20px;top:42px;display:grid;grid-template-columns:1fr 1fr;gap:16px}
.para{position:absolute;left:20px;right:20px;top:40px}
.para p{margin-bottom:6px}

/* boxes row */
.quad{position:absolute;left:0;right:0;top:44px;height:104px;display:grid;grid-template-columns:repeat(4,1fr)}
.quad div{padding:12px 8px;text-align:center;color:var(--white);background:var(--dark)}
.quad div:nth-child(2n){background:var(--orange)}
.quad .ic{width:12px;height:12px;border:1.2px solid #fff;border-radius:50%;margin:0 auto 8px}
.quad p{text-align:left;margin-top:5px}

.panel{position:absolute;background:var(--dark);color:var(--white)}
.orange-panel{position:absolute;background:var(--orange);color:var(--white)}

.diff{left:20px;right:20px;top:40px;height:116px;border-radius:6px;padding:12px}
.diff ul{list-style:none;width:48%}
.diff li{display:flex;gap:6px;align-items:center;margin-bottom:8px}
.diff .icon{flex:none}

.pct{position:absolute;border-radius:50%;display:flex;align-items:center;justify-content:center;color:#fff;font-weight:700}
.trend-list{position:absolute;right:12px;top:54px;width:100px}
.trend-list div{display:flex;gap:6px;margin-bottom:12px}
.trend-list b{font-size:5.5px;display:block;color:var(--ink)}
.trend-list b.o{color:var(--orange)}

.proc{position:absolute;left:14px;right:14px;top:48px}

.divider-title{position:absolute;left:18px;color:#fff;font-weight:700;font-size:18px}
.divider-sub{position:absolute;left:18px;color:#fff;font-size:6px}
.orange-bg{background:linear-gradient(135deg,var(--orange),var(--orange-deep))}

.headline{font-weight:800;color:#fff;font-size:13px;line-height:1.2;text-transform:uppercase}
</style>
</head>
<body>
<main class="sheet">

<!-- 1 Cover -->
<section class="slide cover">
  <div class="brand"><span class="dot"></span><span>NEXORA<small>TECHNOLOGIES</small></span></div>
</section>

<!-- 2 Title -->
<section class="slide dark-bg">
  <div class="brand white top" style="top:52px;font-size:13px"><span class="dot"></span>NEXORA TECHNOLOGIES</div>
  <div class="hero-title" style="top:100px">Your Title Here</div>
  <div class="hero-sub" style="top:128px">Your Subtitle Goes Here</div>
  <div class="hero-url">www.nexoratech.com</div>
  <div class="foot" style="background:#151515"><span></span><span></span></div>
</section>

<!-- 3 Agenda -->
<section class="slide">
  <div class="title">OUR AGENDA</div>
  <div class="agenda">
    <div class="item"><span class="sq"></span><div><b>Agenda One</b><div class="tx">Short note on this topic for the team.</div></div></div>
    <div class="item"><span class="sq"></span><div><b>Agenda Four</b><div class="tx">Short note on this topic for the team.</div></div></div>
    <div class="item"><span class="sq"></span><div><b class="o">Agenda Two</b><div class="tx">Short note on this topic for the team.</div></div></div>
    <div class="item"><span class="sq"></span><div><b class="o">Agenda Five</b><div class="tx">Short note on this topic for the team.</div></div></div>
    <div class="item"><span class="sq"></span><div><b>Agenda Three</b><div class="tx">Short note on this topic for the team.</div></div></div>
    <div class="item"><span class="sq"></span><div><b>Agenda Six</b><div class="tx">Short note on this topic for the team.</div></div></div>
  </div>
  <div class="foot"><span class="mark">NEXORA</span><span>© Copyright Nexora Technologies</span><span>3</span></div>
</section>

<!-- 4 Welcome -->
<section class="slide">
  <div class="ph ph-dark" role="img" aria-label="Photo of a modern office interior" style="left:0;right:0;top:0;height:70px"></div>
  <div style="position:absolute;left:110px;top:54px;width:170px;height:34px;background:#fff;border-radius:4px;display:flex;align-items:center;justify-content:center">
    <span class="brand" style="font-size:18px">NEXORA</span>
  </div>
  <div style="position:absolute;left:0;right:0;top:96px;text-align:center;font-weight:700;font-size:10px">Welcome Message</div>
  <div style="position:absolute;left:40px;top:112px;font-size:22px;font-weight:800;line-height:1">”</div>
  <div class="tx" style="position:absolute;left:60px;right:60px;top:118px">We build reliable systems that help people work better. Thank you for joining us today; here is what we plan to share and why it matters to you and your business.</div>
  <div class="foot"><span class="mark">NEXORA</span><span>© Copyright Nexora Technologies</span><span>4</span></div>
</section>

<!-- 5 Two Column Text -->
<section class="slide">
  <div class="title">Two Column Text</div>
  <div class="two tx">
    <ul class="bul">
      <li>Our services help teams plan, build and run secure digital systems every day.</li>
      <li>We design networks that grow with your needs and stay easy to manage.</li>
      <li>Cloud solutions keep your data safe and ready wherever you work.</li>
      <li>Support staff respond quickly and keep your operations moving forward.</li>
      <li>Training sessions help staff use new tools with confidence.</li>
    </ul>
    <ul class="bul">
      <li>Consulting work starts with a clear review of your current setup.</li>
      <li>We then propose a plan with costs, timelines and clear milestones.</li>
      <li>Projects are delivered in stages so results show early on.</li>
      <li>Each stage is tested, documented and handed over with care.</li>
      <li>Ongoing reviews keep the system aligned with your goals.</li>
    </ul>
  </div>
  <div class="foot"><span class="mark">NEXORA</span><span>© Copyright Nexora Technologies</span><span>5</span></div>
</section>

<!-- 6 Text Slide -->
<section class="slide">
  <div class="title">Text Slide</div>
  <div class="para tx">
    <p>Information technology shapes how companies serve customers, share knowledge and make decisions. Our team brings years of practice across networks, software and support to help clients move faster with less risk.</p>
    <p>We begin every project by listening. Understanding your people, your processes and your goals lets us design systems that fit the way you already work, rather than forcing change for its own sake.</p>
    <p>From there we plan, build and test in short cycles. Each step is visible, measured and open to feedback, so you always know where the project stands and what comes next.</p>
    <p>After launch we stay close. Monitoring, updates and regular reviews keep everything secure, fast and ready for growth over the years ahead.</p>
  </div>
  <div class="foot"><span class="mark">NEXORA</span><span>© Copyright Nexora Technologies</span><span>6</span></div>
</section>

<!-- 7 Chart + Text -->
<section class="slide">
  <div class="title">Chart Slide + Text</div>
  <svg style="position:absolute;left:14px;top:40px" width="200" height="145" viewBox="0 0 200 145">
    <text x="100" y="8" font-size="6" font-weight="700" text-anchor="middle" fill="#222" font-family="Open Sans, sans-serif">Chart Title</text>
    <g stroke="#e4e4e4" stroke-width=".5">
      <line x1="20" y1="20" x2="195" y2="20"/><line x1="20" y1="40" x2="195" y2="40"/><line x1="20" y1="60" x2="195" y2="60"/>
      <line x1="20" y1="80" x2="195" y2="80"/><line x1="20" y1="100" x2="195" y2="100"/><line x1="20" y1="120" x2="195" y2="120"/>
    </g>
    <g font-size="4.5" fill="#777" font-family="Open Sans, sans-serif" text-anchor="end">
      <text x="16" y="22">5</text><text x="16" y="42">4</text><text x="16" y="62">3</text><text x="16" y="82">2</text><text x="16" y="102">1</text><text x="16" y="122">0</text>
    </g>
    <g>
      <rect x="28" y="34" width="7" height="86" fill="#2b2b2b"/><rect x="36" y="72" width="7" height="48" fill="#f7941d"/><rect x="44" y="80" width="7" height="40" fill="#9a9a9a"/>
      <rect x="72" y="70" width="7" height="50" fill="#2b2b2b"/><rect x="80" y="32" width="7" height="88" fill="#f7941d"/><rect x="88" y="80" width="7" height="40" fill="#9a9a9a"/>
      <rect x="116" y="50" width="7" height="70" fill="#2b2b2b"/><rect x="124" y="84" width="7" height="36" fill="#f7941d"/><rect x="132" y="60" width="7" height="60" fill="#9a9a9a"/>
      <rect x="160" y="30" width="7" height="90" fill="#2b2b2b"/><rect x="168" y="64" width="7" height="56" fill="#f7941d"/><rect x="176" y="20" width="7" height="100" fill="#9a9a9a"/>
    </g>
    <g font-size="4.5" fill="#777" font-family="Open Sans, sans-serif" text-anchor="middle">
      <text x="40" y="128">Category 1</text><text x="84" y="128">Category 2</text><text x="128" y="128">Category 3</text><text x="172" y="128">Category 4</text>
    </g>
    <g font-size="4" fill="#777" font-family="Open Sans, sans-serif">
      <rect x="62" y="136" width="4" height="4" fill="#2b2b2b"/><text x="68" y="140">Series 1</text>
      <rect x="90" y="136" width="4" height="4" fill="#f7941d"/><text x="96" y="140">Series 2</text>
      <rect x="118" y="136" width="4" height="4" fill="#9a9a9a"/><text x="124" y="140">Series 3</text>
    </g>
  </svg>
  <ul class="bul tx" style="position:absolute;left:225px;right:20px;top:48px">
    <li>Sales grew steadily across all four categories this year with strong results.</li>
    <li>Category two led the second series thanks to new cloud contracts.</li>
    <li>Support revenue stayed stable and gave the business a firm base.</li>
    <li>We expect further growth next year as new services reach the market.</li>
  </ul>
  <div class="foot"><span class="mark">NEXORA</span><span>© Copyright Nexora Technologies</span><span>7</span></div>
</section>

<!-- 8 Blank -->
<section class="slide">
  <div class="title">Your Blank Slide</div>
  <div class="foot"><span class="mark">NEXORA</span><span>© Copyright Nexora Technologies</span><span>8</span></div>
</section>

<!-- 9 Break -->
<section class="slide">
  <div class="ph" role="img" aria-label="Photo of a bright office corridor" style="inset:0;background:linear-gradient(135deg,#3b3b3b,#6c6c6c 60%,#8a7a64)"></div>
  <div style="position:absolute;left:18px;top:18px;color:#fff;font-weight:800;font-size:18px;line-height:1.1">Break<br>Slide</div>
  <div style="position:absolute;left:18px;top:62px;width:26px;height:2px;background:var(--orange)"></div>
</section>

<!-- 10 Title Here boxes -->
<section class="slide">
  <div class="title">Your Title Here</div>
  <div class="quad tx light">
    <div><span class="ic"></span><span class="h-sm white">Heading Here</span><p>Write a short line about this point for your audience here.</p></div>
    <div><span class="ic"></span><span class="h-sm white">Heading Here</span><p>Write a short line about this point for your audience here.</p></div>
    <div><span class="ic"></span><span class="h-sm white">Heading Here</span><p>Write a short line about this point for your audience here.</p></div>
    <div><span class="ic"></span><span class="h-sm white">Heading Here</span><p>Write a short line about this point for your audience here.</p></div>
  </div>
  <div class="foot"><span class="mark">NEXORA</span><span>© Copyright Nexora Technologies</span><span>10</span></div>
</section>

<!-- 11 Differences -->
<section class="slide">
  <div class="title">Our Differences</div>
  <div class="panel diff tx light">
    <ul>
      <li><span class="icon"></span>Clear plans with fixed costs and honest timelines.</li>
      <li><span class="icon"></span>Local engineers who know your systems well.</li>
      <li><span class="icon"></span>Security built in from the very first day.</li>
      <li><span class="icon"></span>Support that answers quickly, every time.</li>
    </ul>
    <div class="ph ph-hand" role="img" aria-label="Photo of a hand touching a digital network" style="right:12px;top:22px;width:42%;height:72px"></div>
  </div>
  <div class="foot"><span class="mark">NEXORA</span><span>© Copyright Nexora Technologies</span><span>11</span></div>
</section>

<!-- 12 Mockup -->
<section class="slide">
  <div class="panel" style="left:0;top:0;width:170px;height:122px;padding:10px 12px">
    <div style="font-weight:700;font-size:10px">Our Mockup Area</div>
    <div style="width:22px;height:2px;background:var(--orange);margin:3px 0 10px"></div>
    <div class="h-sm white" style="margin-bottom:3px">Heading Here</div>
    <div class="tx light">Show your product on a screen here and add a short note on what it does for clients.</div>
  </div>
  <div class="ph ph-blue" role="img" aria-label="Desktop monitor showing a digital globe" style="left:190px;top:22px;width:190px;height:118px;border:5px solid #1a1a1a;border-radius:3px"></div>
  <div style="position:absolute;left:262px;top:140px;width:46px;height:16px;background:#cfcfcf"></div>
  <div class="tx" style="position:absolute;left:18px;top:134px;width:160px">
    <div style="display:flex;gap:6px;margin-bottom:8px"><span class="icon" style="background:var(--dark);flex:none"></span>Easy to edit screens for any product or service you offer.</div>
    <div style="display:flex;gap:6px"><span class="icon" style="flex:none"></span>Swap in your own screenshot and keep the rest as is.</div>
  </div>
  <div class="foot"><span class="mark">NEXORA</span><span>© Copyright Nexora Technologies</span><span>12</span></div>
</section>

<!-- 13 Brand Detailed -->
<section class="slide">
  <div class="title">Brand Detailed</div>
  <div class="ph ph-blue" role="img" aria-label="Photo of a glowing digital network" style="left:20px;top:42px;width:110px;height:58px"></div>
  <div class="ph ph-hand" role="img" aria-label="Photo of a hand with floating data points" style="left:20px;top:102px;width:110px;height:58px"></div>
  <div style="position:absolute;left:132px;top:42px;width:240px;height:118px;display:grid;grid-template-columns:1fr 1fr;gap:2px;text-align:center">
    <div style="background:var(--dark);padding:10px"><div class="h-sm white">Sponsor</div><div class="tx light">A short line about this part of the brand.</div></div>
    <div style="background:var(--orange);padding:10px"><div class="h-sm white">Technology</div><div class="tx light">A short line about this part of the brand.</div></div>
    <div style="background:var(--dark);padding:10px"><div class="h-sm white">Industry</div><div class="tx light">A short line about this part of the brand.</div></div>
    <div style="background:var(--orange);padding:10px"><div class="h-sm white">Digital</div><div class="tx light">A short line about this part of the brand.</div></div>
  </div>
  <div class="foot"><span class="mark">NEXORA</span><span>© Copyright Nexora Technologies</span><span>13</span></div>
</section>

<!-- 14 Trending -->
<section class="slide">
  <div class="title">Trending In The World</div>
  <div class="ph" role="img" aria-label="World map" style="left:14px;top:44px;width:250px;height:130px;background:linear-gradient(180deg,#c9c9c9,#b2b2b2);border-radius:30px"></div>
  <div class="pct" style="left:14px;top:100px;width:24px;height:24px;background:#555;font-size:7px">25%</div>
  <div class="pct" style="left:86px;top:80px;width:36px;height:36px;background:var(--orange);font-size:10px">80%</div>
  <div class="pct" style="left:180px;top:86px;width:34px;height:34px;background:var(--orange);font-size:10px">75%</div>
  <div class="pct" style="left:150px;top:128px;width:22px;height:22px;background:#333;font-size:6px">15%</div>
  <div class="trend-list tx">
    <div><span class="icon" style="flex:none"></span><div><b>Conference</b>Short note here for this item.</div></div>
    <div><span class="icon" style="flex:none"></span><div><b class="o">Insight</b>Short note here for this item.</div></div>
    <div><span class="icon" style="flex:none;background:var(--dark)"></span><div><b>Performance</b>Short note here for this item.</div></div>
  </div>
  <div class="foot"><span class="mark">NEXORA</span><span>© Copyright Nexora Technologies</span><span>14</span></div>
</section>

<!-- 15 Right Image + Text -->
<section class="slide">
  <div class="title">Right Image + Text</div>
  <div class="tx" style="position:absolute;left:20px;top:44px;width:190px">
    <div class="h-sm" style="margin-bottom:5px">Heading Here</div>
    <ul class="bul">
      <li>We help your teams adopt new tools without slowing daily work down.</li>
      <li>Every plan begins with a clear look at what you already have.</li>
      <li>Results are shared in simple reports that anyone can follow.</li>
      <li>Our engineers stay on call for urgent issues around the clock.</li>
      <li>Regular reviews keep the system secure, fast and current.</li>
    </ul>
  </div>
  <div class="ph ph-city" role="img" aria-label="Photo of a person at a window overlooking a city" style="left:228px;top:40px;width:152px;height:120px"></div>
  <div class="foot"><span class="mark">NEXORA</span><span>© Copyright Nexora Technologies</span><span>15</span></div>
</section>

<!-- 16 Title Goes Here photos -->
<section class="slide">
  <div class="title">Your Title Goes Here</div>
  <div class="ph ph-blue" role="img" aria-label="Photo of a digital network" style="left:20px;top:44px;width:82px;height:56px"></div>
  <div class="ph ph-hand" role="img" aria-label="Photo of a glowing light in a hand" style="left:104px;top:44px;width:50px;height:56px"></div>
  <div class="ph ph-blue" role="img" aria-label="Photo of a glass office building" style="left:20px;top:102px;width:60px;height:58px"></div>
  <div class="ph ph-city" role="img" aria-label="Photo of a city skyline" style="left:82px;top:102px;width:72px;height:58px"></div>
  <div class="panel tx light" style="left:172px;top:56px;width:200px;height:96px;padding:14px 16px;text-align:center">
    <div class="h-sm white" style="font-size:8px;margin-bottom:6px">Heading Goes Here</div>
    A short paragraph that explains the idea behind these images and how it links to the services your company offers to clients every day.
  </div>
  <div class="foot"><span class="mark">NEXORA</span><span>© Copyright Nexora Technologies</span><span>16</span></div>
</section>

<!-- 17 Dark Divider -->
<section class="slide dark-bg">
  <div class="brand white" style="position:absolute;left:18px;top:96px;font-size:11px"><span class="dot"></span>NEXORA TECHNOLOGIES</div>
  <div class="divider-title" style="top:124px">Your Divider</div>
  <div class="divider-sub" style="top:148px;color:#ccc">Your Subtitle Goes Here</div>
</section>

<!-- 18 Left Image + Text -->
<section class="slide">
  <div class="title">Left Image + Text</div>
  <div class="ph ph-warm" role="img" aria-label="Photo of a person working at a computer" style="left:20px;top:42px;width:140px;height:104px"></div>
  <ul class="bul tx" style="position:absolute;left:176px;right:20px;top:44px">
    <li>We help your teams adopt new tools without slowing daily work down.</li>
    <li>Every plan begins with a clear look at what you already have.</li>
    <li>Results are shared in simple reports anyone can follow.</li>
    <li>Our engineers stay on call for urgent issues around the clock.</li>
    <li>Regular reviews keep the system secure, fast and current.</li>
  </ul>
  <div class="foot"><span class="mark">NEXORA</span><span>© Copyright Nexora Technologies</span><span>18</span></div>
</section>

<!-- 19 Bullets And Image -->
<section class="slide">
  <div class="title">Bullets And Image</div>
  <ul class="bul tx" style="position:absolute;left:20px;top:44px;width:190px">
    <li>Connected devices share data safely across your whole office network.</li>
    <li>Smart dashboards show what is working and what needs attention.</li>
    <li>Remote access keeps teams productive from any location.</li>
    <li>Automatic backups protect your records from loss or damage.</li>
    <li>Our team checks each system to keep it fast and reliable.</li>
  </ul>
  <div style="position:absolute;right:0;top:22px;width:70px;height:150px;background:var(--dark)"></div>
  <div class="ph ph-blue" role="img" aria-label="Photo of a hand touching connected technology icons" style="left:228px;top:34px;width:150px;height:118px"></div>
  <div class="foot"><span class="mark">NEXORA</span><span>© Copyright Nexora Technologies</span><span>19</span></div>
</section>

<!-- 20 Images + Text -->
<section class="slide">
  <div class="title">Images + Text</div>
  <div class="ph ph-warm" role="img" aria-label="Photo of business people shaking hands" style="left:0;top:40px;width:196px;height:58px"></div>
  <div class="orange-panel tx light" style="left:198px;top:40px;width:200px;height:58px;padding:10px 14px">Partners trust us to keep their systems running. A short line goes here. Another brief note about this service fits here too.</div>
  <div class="panel" style="left:0;top:100px;width:196px;height:70px;padding:14px;font-size:6.5px;line-height:1.5">A short statement about your services goes here with a clear message for the reader.</div>
  <div class="ph ph-city" role="img" aria-label="Photo of a city skyline" style="left:198px;top:100px;width:200px;height:70px"></div>
  <div class="foot"><span class="mark">NEXORA</span><span>© Copyright Nexora Technologies</span><span>20</span></div>
</section>

<!-- 21 Process -->
<section class="slide">
  <div class="title">Process</div>
  <svg class="proc" width="370" height="110" viewBox="0 0 370 110" font-family="Open Sans, sans-serif">
    <g fill="none" stroke="#bbb" stroke-width=".8" stroke-dasharray="2 2">
      <path d="M36 28 A40 40 0 0 1 110 28"/><path d="M110 92 A40 40 0 0 0 184 92"/>
      <path d="M184 28 A40 40 0 0 1 258 28"/><path d="M258 92 A40 40 0 0 0 332 92"/>
    </g>
    <g font-size="5" font-weight="700" fill="#222" text-anchor="middle">
      <text x="36" y="10">Your Title Here</text><text x="184" y="10">Your Title Here</text><text x="332" y="10">Your Title Here</text>
      <text x="110" y="108">Your Title Here</text><text x="258" y="108">Your Title Here</text>
    </g>
    <circle cx="36" cy="60" r="15" fill="#555"/>
    <circle cx="110" cy="60" r="15" fill="#f7941d"/>
    <circle cx="184" cy="60" r="15" fill="#2b2b2b"/>
    <circle cx="258" cy="60" r="15" fill="#f7941d"/>
    <circle cx="332" cy="60" r="15" fill="#e8810c"/>
    <g stroke="#fff" stroke-width="1.4" fill="none">
      <path d="M30 60 h12 M38 56 l4 4 -4 4"/><path d="M104 60 h12 M112 56 l4 4 -4 4"/><path d="M178 60 h12 M186 56 l4 4 -4 4"/><path d="M252 60 h12 M260 56 l4 4 -4 4"/><path d="M327 60 l3 3 6 -6"/>
    </g>
  </svg>
  <div class="tx" style="position:absolute;left:20px;right:20px;top:168px">Each stage builds on the last: we review, plan, build, test and then support your system so it keeps working well for years to come.</div>
  <div class="foot"><span class="mark">NEXORA</span><span>© Copyright Nexora Technologies</span><span>21</span></div>
</section>

<!-- 22 Turn processes -->
<section class="slide">
  <div class="ph" role="img" aria-label="Photo of a hand reaching toward a digital network" style="inset:0;background:linear-gradient(100deg,#f7941d 0%,#c26f12 38%,#23344a 70%,#0e1a28 100%)"></div>
  <div style="position:absolute;left:14px;top:66px;width:170px">
    <div class="headline">Turn your processes into competitive advantage</div>
    <div class="tx light" style="margin-top:6px">Smart systems save time and cut costs. A short supporting line goes here for the reader.</div>
    <div class="tx light" style="margin-top:4px">Another short line to close the thought clearly.</div>
  </div>
  <div class="foot"><span class="mark">NEXORA</span><span>© Copyright Nexora Technologies</span><span>22</span></div>
</section>

<!-- 23 Market Overview -->
<section class="slide">
  <div class="title">Market Overview</div>
  <div class="panel tx light" style="left:14px;top:40px;width:76px;height:92px;padding:6px 8px">
    <div class="h-sm white">Heading Text</div>A short note about this market point.
    <div class="h-sm white" style="margin-top:14px">Heading Text</div>A short note here.
  </div>
  <div class="ph ph-city" role="img" aria-label="Photo of a robot hand" style="left:92px;top:40px;width:80px;height:92px"></div>
  <svg style="position:absolute;left:182px;top:50px" width="64" height="64" viewBox="0 0 64 64" font-family="Open Sans, sans-serif">
    <circle cx="32" cy="32" r="26" fill="none" stroke="#e3e3e3" stroke-width="8"/>
    <circle cx="32" cy="32" r="26" fill="none" stroke="#f7941d" stroke-width="8" stroke-dasharray="98 163" transform="rotate(-90 32 32)"/>
    <circle cx="32" cy="32" r="19" fill="#f7941d"/>
    <text x="32" y="36" font-size="11" font-weight="700" fill="#fff" text-anchor="middle">60%</text>
  </svg>
  <div class="panel tx light" style="left:256px;top:40px;width:128px;height:92px;padding:8px 10px">
    <div class="h-sm white">Heading Text</div>A short note about this market trend.
    <div class="h-sm white" style="margin-top:8px">Heading Text</div>Another short note about this trend.
  </div>
  <div class="tx" style="position:absolute;left:14px;right:14px;top:140px">
    <div class="h-sm">Heading Text</div>
    The market for managed IT keeps growing as firms move to the cloud. Demand is strongest in security, data and support services, where we see room to grow our share over the next few years.
  </div>
  <div class="foot"><span class="mark">NEXORA</span><span>© Copyright Nexora Technologies</span><span>23</span></div>
</section>

<!-- 24 Orange Divider -->
<section class="slide orange-bg">
  <div class="brand white" style="position:absolute;right:24px;top:70px;font-size:12px"><span class="dot"></span>NEXORA TECHNOLOGIES</div>
  <div class="divider-title" style="top:140px">Your Divider</div>
  <div class="divider-sub" style="top:164px">Subtitle Here</div>
</section>

<!-- 25 Title Goes Here grid -->
<section class="slide">
  <div class="title">Your Title Goes Here</div>
  <div style="position:absolute;left:18px;right:18px;top:48px;height:116px;display:grid;grid-template-columns:1fr 1fr 1fr;grid-template-rows:1fr 1fr;gap:2px">
    <div class="ph-blue" role="img" aria-label="Photo of people at a laptop" style="position:relative"></div>
    <div style="background:var(--orange);padding:8px;text-align:center"><div class="h-sm white" style="font-size:7px">Heading Goes Here</div><div class="tx light">Short text for this point.</div></div>
    <div class="ph-hand" role="img" aria-label="Photo of a tablet with charts" style="position:relative"></div>
    <div style="background:var(--dark);padding:8px;text-align:center"><div class="h-sm white" style="font-size:7px">Heading Goes Here</div><div class="tx light">Short text for this point.</div></div>
    <div class="ph-blue" role="img" aria-label="Photo of a digital network" style="position:relative"></div>
    <div style="background:var(--dark);padding:8px;text-align:center"><div class="h-sm white" style="font-size:7px">Heading Goes Here</div><div class="tx light">Short text for this point.</div></div>
  </div>
  <div class="foot"><span class="mark">NEXORA</span><span>© Copyright Nexora Technologies</span><span>25</span></div>
</section>

<!-- 26 Pestel -->
<section class="slide">
  <div class="title">Pestel Diagram</div>
  <svg style="position:absolute;left:0;top:0" width="398" height="215" viewBox="0 0 398 215" font-family="Open Sans, sans-serif">
    <defs><polygon id="hex" points="0,-22 19,-11 19,11 0,22 -19,11 -19,-11"/></defs>
    <g fill="#f7941d">
      <use href="#hex" x="180" y="85"/><use href="#hex" x="218" y="85"/>
      <use href="#hex" x="237" y="118"/><use href="#hex" x="218" y="151"/>
      <use href="#hex" x="180" y="151"/><use href="#hex" x="161" y="118"/>
    </g>
    <use href="#hex" x="199" y="118" fill="#fff" stroke="#f7941d" stroke-width="1.5"/>
    <g font-size="4.5" fill="#fff" text-anchor="middle" font-weight="600">
      <text x="180" y="87">Legal</text><text x="218" y="87">Politics</text><text x="237" y="120">Economic</text>
      <text x="218" y="153">Social</text><text x="180" y="153">Technology</text><text x="161" y="120">Environment</text>
    </g>
    <g font-size="5" font-weight="700">
      <text x="240" y="58" fill="#222">Politics</text><text x="270" y="100" fill="#222">Economic</text><text x="262" y="150" fill="#f7941d">Social</text>
      <text x="125" y="76" fill="#222">Legal</text><text x="100" y="128" fill="#222">Environment</text><text x="170" y="188" fill="#222">Technology</text>
    </g>
    <g font-size="4" fill="#777">
      <text x="240" y="65">A short note for this factor.</text><text x="270" y="107">A short note for this factor.</text><text x="262" y="157">A short note for this factor.</text>
      <text x="92" y="83">A short note for this factor.</text><text x="72" y="135">A short note for this factor.</text><text x="150" y="195">A short note for this factor.</text>
    </g>
  </svg>
  <div class="foot"><span class="mark">NEXORA</span><span>© Copyright Nexora Technologies</span><span>26</span></div>
</section>

<!-- 27 Company Structure -->
<section class="slide">
  <div class="title">Company Structure</div>
  <svg style="position:absolute;left:0;top:0" width="398" height="215" viewBox="0 0 398 215" font-family="Open Sans, sans-serif">
    <g stroke="#555" stroke-width=".6" fill="none">
      <path d="M199 68 v10 M110 78 h178 M110 78 v8 M199 78 v8 M288 78 v8"/>
      <path d="M199 98 v14 M64 112 h270 M64 112 v10 M154 112 v10 M244 112 v10 M334 112 v10"/>
    </g>
    <rect x="169" y="56" width="60" height="12" fill="#2b2b2b"/>
    <rect x="80" y="86" width="60" height="12" fill="#f7941d"/><rect x="169" y="86" width="60" height="12" fill="#f7941d"/><rect x="258" y="86" width="60" height="12" fill="#f7941d"/>
    <rect x="34" y="122" width="60" height="14" fill="#2b2b2b"/><rect x="124" y="122" width="60" height="14" fill="#fff"/><rect x="214" y="122" width="60" height="14" fill="#fff"/><rect x="304" y="122" width="60" height="14" fill="#2b2b2b"/>
    <g font-size="4.5" text-anchor="middle" font-weight="600">
      <text x="199" y="64" fill="#fff">General Manager</text>
      <text x="110" y="94" fill="#fff">Division Manager</text><text x="199" y="94" fill="#fff">Division Manager</text><text x="288" y="94" fill="#fff">Division Manager</text>
      <text x="64" y="128" fill="#fff">Department</text><text x="64" y="133" fill="#fff">of Commerce</text>
      <text x="154" y="128" fill="#222">Financial</text><text x="154" y="133" fill="#222">Department</text>
      <text x="244" y="128" fill="#222">Administrative</text><text x="244" y="133" fill="#222">Department</text>
      <text x="334" y="131" fill="#fff">Workshop</text>
    </g>
  </svg>
  <div class="foot"><span class="mark">NEXORA</span><span>© Copyright Nexora Technologies</span><span>27</span></div>
</section>

<!-- 28 Orange Divider 2 -->
<section class="slide orange-bg">
  <div class="brand white" style="position:absolute;left:18px;top:86px;font-size:12px"><span class="dot"></span>NEXORA TECHNOLOGIES</div>
  <div class="divider-title" style="top:112px">Your Divider</div>
  <div class="divider-sub" style="top:136px">Your Subtitle Goes Here</div>
</section>

<!-- 29 Turn processes 2 -->
<section class="slide" style="background:var(--darker)">
  <div class="ph" role="img" aria-label="Illustration of a glowing brain on a circuit board" style="left:0;top:0;width:190px;height:216px;background:linear-gradient(160deg,#0b2a4a,#1f6aa0 55%,#0a1c30)"></div>
  <div style="position:absolute;left:200px;top:62px;width:180px">
    <div class="headline" style="font-size:11px">Turn your processes into competitive advantage</div>
    <div class="tx light" style="margin-top:6px">Smart systems save time and cut costs. A short supporting line goes here for the reader.</div>
    <div class="tx light" style="margin-top:4px">Another short line to close the thought clearly for your audience.</div>
  </div>
  <div class="foot"><span class="mark">NEXORA</span><span>© Copyright Nexora Technologies</span><span>29</span></div>
</section>

<!-- 30 Thank you -->
<section class="slide dark-bg">
  <div class="brand white" style="position:absolute;left:18px;top:54px;font-size:13px"><span class="dot"></span>NEXORA TECHNOLOGIES</div>
  <div style="position:absolute;left:18px;top:86px;color:#fff;font-weight:700;font-size:20px">Thank you..</div>
  <div class="tx light" style="position:absolute;left:18px;top:114px;width:180px">A short closing line with thanks to your audience.</div>
  <div class="hero-url">www.nexoratech.com</div>
</section>

</main>
</body>
</html>
```